Investment Group needs a web page design

We need a web page design for a San Francisco-based investment group called 'Valtrimor LLC'. The final design should be stylish and attractive to the idea while retaining a sense of stability and professionalism. A great example is http://brindlewoodholdings.com/.

I am attaching the group's logo which should be the base for the webpage design.
Updates

Please note that I am interested in a single webpage that presents basic information. See the following example: http://brindlewoodholdings.com/

Target Market(s)

persons doing initial due diligence and trying to assess what kind of group we are.

Industry/Entity Type

Investment

Font styles to use
Serif

Colors
86acd3
3176b5
0355a3

Requirements
Nice to have
• Would love the design to incorporate the concept - 'Sen no Sen: a block and counter attack while the opponent is attacking.'
Should not have
• Do not include trite illustrations related to finance, money or investing.

```html
<!DOCTYPE html>
<html lang="en">
<head>
<meta charset="utf-8">
<title>Valtrimor LLC</title>
<link href="https://fonts.googleapis.com/css2?family=Open+Sans:wght@300;400&display=swap" rel="stylesheet">
<style>
  :root {
    --brand-blue: #0355a3;
    --panel-blue: rgba(16, 92, 176, 0.95);
    --card-white: #ffffff;
    --ink: #111111;
    --rule: #e8e8e8;
    --sky: #5b6266;
    --sky-low: #6a7372;
    --swell: #a4aba7;
    --sea: #4b5753;
    --sea-light: #7d8783;
    --foam: #c7cbc7;
    --foam-light: #e4e6e2;
  }
  * { margin: 0; padding: 0; box-sizing: border-box; }
  html, body { width: 1200px; height: 703px; overflow: hidden; }
  body { font-family: "Open Sans", Arial, sans-serif; color: var(--ink); }

  .page { position: relative; width: 1200px; height: 703px; overflow: hidden; }

  .hero-photo {
    position: absolute; inset: 0;
    background: linear-gradient(180deg,
      var(--sky) 0%,
      var(--sky-low) 24%,
      var(--swell) 31%,
      var(--sea) 44%,
      var(--sea-light) 60%,
      var(--foam) 78%,
      var(--foam-light) 100%);
  }

  .contact-card {
    position: absolute; left: 133px; top: 96px; width: 262px; height: 513px;
    background: var(--card-white);
    clip-path: polygon(12px 0, 250px 0, 262px 12px, 262px 513px, 12px 513px, 0 501px, 0 12px);
    text-align: center;
  }
  .contact-card .corner-mark { position: absolute; right: 0; bottom: 0; }

  .brand { position: absolute; left: 20px; top: 38px; width: 222px; display: flex; align-items: center; gap: 6px; }
  .brand-square { width: 31px; height: 31px; background: var(--ink); flex: none; }
  .brand-name { font-size: 31px; font-weight: 400; letter-spacing: 0.3px; color: var(--ink); line-height: 1; }

  .contact-item { position: absolute; left: 0; width: 262px; font-size: 13px; line-height: 19.5px; }
  .contact-item svg { display: block; margin: 0 auto; }
  .item-address { top: 144px; }
  .item-address svg { margin-bottom: 14px; }
  .item-phone { top: 272px; }
  .item-phone svg { margin-bottom: 16px; }
  .item-email { top: 353px; }
  .item-email svg { margin-bottom: 17px; }
  .rule { position: absolute; left: 42px; width: 178px; height: 1px; background: var(--rule); }
  .rule-1 { top: 253px; }
  .rule-2 { top: 336px; }

  .legal { position: absolute; left: 0; bottom: 12px; width: 262px; font-size: 10.5px; }

  .feature-panel {
    position: absolute; left: 714px; top: 476px; width: 352px; height: 133px;
    background: var(--panel-blue); color: #fff; padding: 17px 16px 0 25px;
  }
  .feature-panel h2 { font-weight: 300; font-size: 19.5px; line-height: 26px; margin-bottom: 6px; }
  .feature-panel p { font-size: 11.4px; line-height: 17.5px; margin-left: 2px; }
  .feature-panel .corner-mark { position: absolute; right: 0; bottom: 0; }
</style>
</head>
<body>
<main class="page">
  <div class="hero-photo" role="img" aria-label="Windsurfer with a red and white sail carving through a breaking wave under a grey sky"></div>

  <aside class="contact-card">
    <div class="brand">
      <span class="brand-square"></span>
      <span class="brand-name">VALTRIMOR</span>
    </div>

    <div class="contact-item item-address">
      <svg width="18" height="24" viewBox="0 0 18 24" aria-hidden="true">
        <path d="M9 0C4 0 0 4 0 9c0 6.5 9 15 9 15s9-8.5 9-15c0-5-4-9-9-9z" fill="var(--brand-blue)"/>
        <circle cx="9" cy="9" r="3.2" fill="#fff"/>
      </svg>
      Address lane1 goes here,<br>Street Name, State,<br>Zipcode-123456
    </div>
    <div class="rule rule-1"></div>

    <div class="contact-item item-phone">
      <svg width="20" height="20" viewBox="0 0 24 24" aria-hidden="true">
        <path d="M6.6 10.8c1.4 2.8 3.8 5.1 6.6 6.6l2.2-2.2c.3-.3.7-.4 1-.2 1.1.4 2.3.6 3.6.6.6 0 1 .4 1 1V20c0 .6-.4 1-1 1C10.6 21 3 13.4 3 4c0-.6.4-1 1-1h3.5c.6 0 1 .4 1 1 0 1.3.2 2.5.6 3.6.1.3 0 .7-.2 1z" fill="var(--brand-blue)"/>
      </svg>
      123 456 7890
    </div>
    <div class="rule rule-2"></div>

    <div class="contact-item item-email">
      <svg width="22" height="16" viewBox="0 0 22 16" aria-hidden="true">
        <rect width="22" height="16" fill="var(--brand-blue)"/>
        <path d="M1 1l10 8 10-8M1 15l7-6M21 15l-7-6" stroke="#fff" stroke-width="1.3" fill="none"/>
      </svg>
      help@valtrimor.com
    </div>

    <p class="legal">All rights reserved@ 2014.</p>
    <svg class="corner-mark" width="16" height="16" viewBox="0 0 16 16" aria-hidden="true">
      <polygon points="16,0 16,16 0,16" fill="var(--brand-blue)"/>
    </svg>
  </aside>

  <section class="feature-panel">
    <h2>Proper Header Goes Here</h2>
    <p>Fusce ornare lectus vitae purus rhoncus pretium. Donec at quam eros. Integer sed posuere neque. Sed in consequat sapien, sit amet sodales lectus.</p>
    <svg class="corner-mark" width="16" height="16" viewBox="0 0 16 16" aria-hidden="true">
      <polygon points="16,0 16,16 0,16" fill="#ffffff"/>
    </svg>
  </section>
</main>
</body>
</html>
```